Parallax site with a story.

Hi!

This project is to create a website for a restaurant.

Inspiration you can get from
http://www.brevik-solhagen.com/catering/
http://www.kavu-restaurant.com/
http://www.tobelgrenrestaurant.se/fine-dining/
http://www.elcorsotaberna.com/lima/

I have written a pdf that is attached. Please read that for more info.

I would LOVE to have the website made witin parallax like this website: http://www.brevik-solhagen.com/se/

I have made a preliminary logotype and drawed some pictures, how it can look. Is an example- you maybe can improve it if you think its needed.

I will be available 24/7 from now for any question about project.
Updates

Reason: The project has been to a slow start, so I am increasing the deadline time of the project. Thanks

Reason: Hi! Site has been a bit slow unfortunately - I will do the following. I will scetch up a new descrition of project which will involve much less animation. will come back with this tomorrow.

Hi!

Please see descpriton

Hi Everybody!

I have decided to wait with the pictures (page 6 in pdf) and focus on these parts:

1) Create a website with inspiration from the two websites i wrote about in description
2) http://glimmerlund.tavbok.se/   I want to add bookingsystem like this. 
http://www.glimmerlund.com/  (click "Boka" to see it live).
3) A contact form for visitors to post message that is sent to me. (name, number, company, text)

The past animation/parallax is totally replaced by this.  And

Reason: Because I need time to organize your work. I have understood that you have difficulties to understand my idea or vision. I have to givemore information to you, and that's why I'm extending the time.

Target Market(s)

35+ people with intesting in fine bistro dining.

Industry/Entity Type

Restaurant

Requirements
Must have
• Nice design. See page 4 for example of artwork in photoshop needed.

Also system for booking a table, or booking catering also important
Should not have
• It should not relate to "cheap tex mex".

```html
<!DOCTYPE html>
<html lang="en">
<head>
<meta charset="utf-8">
<title>Tambora Restaurant – Catering</title>
<link rel="stylesheet" href="https://fonts.googleapis.com/css2?family=Quicksand:wght@400;500;700&display=swap">
<style>
  :root {
    --brand-dark: #4a1f24;
    --white: #ffffff;
    --panel: rgba(10, 6, 4, 0.5);
    --rule: rgba(255, 255, 255, 0.75);
    --field-text: #c9c9c9;
    --btn-top: #ffb400;
    --btn-bottom: #f07c00;
    --accent-line: #c65a1c;
    --photo-deep: #2a1208;
    --photo-mid: #7a3a12;
    --photo-warm: #c97a2a;
  }
  * { box-sizing: border-box; margin: 0; padding: 0; }
  html, body { width: 1200px; height: 895px; overflow: hidden; background: var(--white); }
  body { position: relative; font-family: "Quicksand", sans-serif; color: var(--white); }

  .site-header { position: absolute; left: 0; top: 0; width: 1200px; height: 166px; background: var(--white); }
  .brand { position: absolute; left: 0; right: 0; top: 58px; display: flex; justify-content: center; align-items: center; gap: 12px; }
  .brand-dot { width: 30px; height: 30px; border-radius: 50%; background: var(--brand-dark); }
  .brand-name { font-size: 32px; font-weight: 700; color: var(--brand-dark); }

  .hero { position: absolute; left: 0; top: 166px; width: 1200px; height: 707px; }
  .hero-photo { position: absolute; inset: 0;
    background:
      radial-gradient(ellipse at 50% 25%, rgba(230,160,70,0.55), transparent 55%),
      radial-gradient(ellipse at 90% 40%, rgba(220,150,60,0.5), transparent 40%),
      radial-gradient(ellipse at 10% 45%, rgba(200,120,40,0.45), transparent 40%),
      linear-gradient(180deg, var(--photo-mid) 0%, var(--photo-warm) 35%, var(--photo-mid) 65%, var(--photo-deep) 100%); }

  .welcome-panel { position: absolute; left: 281px; top: 56px; width: 651px; height: 604px; background: var(--panel); text-align: center; }
  .panel-base-line { position: absolute; left: 553px; top: 659px; width: 200px; height: 2px; background: var(--accent-line); }

  .kicker { position: absolute; left: 0; right: 0; top: 30px; font-size: 24px; letter-spacing: 1px; }
  .title { position: absolute; left: 0; right: 0; top: 70px; font-size: 56px; font-weight: 400; letter-spacing: 2px; line-height: 1; }
  .subtitle { position: absolute; left: 0; right: 0; top: 146px; font-size: 26px; letter-spacing: 1px; }
  .divider { position: absolute; left: 37px; width: 577px; top: 196px; height: 1px; background: var(--rule); }
  .intro { position: absolute; left: 20px; right: 20px; top: 210px; font-size: 18px; line-height: 23px; font-weight: 500; }
  .contact-heading { position: absolute; left: 0; right: 0; top: 282px; font-size: 26px; letter-spacing: 1px; }
  .contact-line { position: absolute; left: 0; right: 0; font-size: 17px; font-weight: 500; letter-spacing: 0.5px; display: flex; justify-content: center; align-items: center; gap: 8px; }
  .contact-line.phone { top: 325px; }
  .contact-line.email { top: 357px; }
  .or { position: absolute; left: 0; right: 0; top: 391px; font-size: 26px; }

  .contact-form { position: absolute; left: 0; right: 0; top: 436px; }
  .field { position: absolute; top: 0; width: 212px; height: 36px; border: none; background: var(--white); text-align: center; font-family: "Quicksand", sans-serif; font-size: 20px; color: var(--field-text); line-height: 36px; }
  .field.name { left: 98px; }
  .field.address { left: 335px; }
  .contact-button { position: absolute; left: 217px; top: 57px; width: 211px; height: 43px; border: none; background: linear-gradient(180deg, var(--btn-top), var(--btn-bottom)); color: var(--white); font-family: "Quicksand", sans-serif; font-size: 26px; letter-spacing: 1px; }

  .slider-dots { position: absolute; left: 0; right: 0; top: 558px; display: flex; justify-content: center; gap: 9px; }
  .slider-dots span { width: 13px; height: 13px; border-radius: 50%; border: 3px solid var(--white); background: transparent; }
</style>
</head>
<body>
  <header class="site-header">
    <div class="brand">
      <span class="brand-dot"></span>
      <span class="brand-name">Tambora Restaurant</span>
    </div>
  </header>

  <section class="hero">
    <div class="hero-photo" role="img" aria-label="Warm, wood-panelled restaurant dining room with red chairs and set tables"></div>

    <div class="welcome-panel">
      <p class="kicker">WELCOME TO</p>
      <h1 class="title">TAMBORA</h1>
      <p class="subtitle">CATERING</p>
      <div class="divider"></div>
      <p class="intro">Catering for weddings, private parties, corporate events, and the sailing fraternity at Cowes has made Harbour Table Catering</p>

      <h2 class="contact-heading" style="font-weight:400">CONTACT US</h2>
      <p class="contact-line phone">
        <svg width="18" height="16" viewBox="0 0 18 16" aria-hidden="true"><path d="M1 5 Q9 -1 17 5 L15 7 L12 6 L12 4 Q9 3 6 4 L6 6 L3 7 Z" fill="#fff"/><rect x="4" y="8" width="10" height="7" rx="1" fill="#fff"/><circle cx="9" cy="11.5" r="2" fill="#3a2010"/></svg>
        ( 0283 ) 5820 417
      </p>
      <p class="contact-line email">
        <svg width="20" height="13" viewBox="0 0 20 13" aria-hidden="true"><rect x="0.5" y="0.5" width="19" height="12" fill="#fff"/><path d="M1 1 L10 8 L19 1" stroke="#3a2010" stroke-width="1.2" fill="none"/></svg>
        contact@tambora.com
      </p>
      <p class="or">OR</p>

      <form class="contact-form">
        <input class="field name" type="text" placeholder="name">
        <input class="field address" type="text" placeholder="address">
        <button class="contact-button" type="button">CONTACT</button>
      </form>

      <div class="slider-dots"><span></span><span></span><span></span></div>
    </div>
    <div class="panel-base-line"></div>
  </section>
</body>
</html>
```